Bright Leaf Company Needs New Packaging Design

We need a design to print directly on our stand up zip pouches, 6x9x3 in., to replace the labels we were applying on generic matte black pouches.

We'd like to keep the current color theme of matte black + [Flavor Color] (in this case, fushia) to communicate the idea of modern, luxury brand (please see velmora coffee brand) and stay somewhat close to the current label so our product will be recognized by actual customers. Other flavors will be a declination of the same layout, matte black + [flavor color]. Colors used should be vibrant, eye catching, to stand out from competition.

We also want to display the actual tea blend picture on the packaging so the consumer can see how beautiful the tea is. The font size for Quince Marigold Verbena should be big enough so it's readable when the product is seen in thumbnail format.

The front should have a seal/stamp close to a top corner with a big "100% Freshness Guarantee",

The company logo "The Brew Works" should be present on the front in a prominent spot. It's provided in the zip file from old label.

We need to display the net weight (4oz / 113g) and number of servings (makes 60 cups). Please refer to old label.

On the back side we need a space for the UPC barcode at the bottom, the company address, a space for the brand's story/mission, steeping instructions with icons (see current label), ingredients and another section featuring our other products. All fonts should be 10pt or bigger.

Artwork of the current label current label is available here
https://files.example-share.net/folders/7Qx2mR9pLk4vNw8sTz3yHc6bJd?key=1-P58rbnVtLKS2wXhyQfme&mode=view

Target Market(s)

USA market, Women ages 25-45, young & young at heart, trendy, health conscious, luxury

Industry/Entity Type

Premium Loose Leaf Tea

Font styles to use
Other font styles liked:
• fonts provided in zip file

Colors
E54698
E96AAD
F1A4CE
F9D9EA
FCEFF6

Requirements
Must have
• See description
Should not have
• Asian look and feel

```html
<!DOCTYPE html>
<html lang="en">
<head>
<meta charset="utf-8">
<title>The Brew Works – Quince Marigold Verbena Tea Pouch</title>
<link rel="stylesheet" href="https://fonts.googleapis.com/css2?family=Signika:wght@500;600&family=Merriweather+Sans:ital,wght@1,400;1,600&family=Alegreya:wght@400;700&display=swap">
<style>
  :root {
    --matte-black: #161616;
    --fuchsia: #E54698;
    --fuchsia-soft: #E96AAD;
    --blush: #F1A4CE;
    --white: #ffffff;
    --grey-text: #d8d8d8;
    --canvas: #ffffff;
  }
  * { box-sizing: border-box; margin: 0; padding: 0; }
  html, body { width: 1200px; height: 1200px; overflow: hidden; background: var(--canvas); }
  body { position: relative; font-family: "Alegreya", serif; }

  .panel {
    position: absolute; top: 236px; width: 465px; height: 728px;
    background: var(--matte-black); color: var(--white); overflow: hidden;
  }
  .panel--front { left: 110px; }
  .panel--back { left: 625px; }

  /* Brand name block */
  .brand-tab {
    position: absolute; left: 165px; top: 0; width: 132px; height: 146px;
    background: var(--fuchsia); display: flex; align-items: center; justify-content: center;
    text-align: center;
  }
  .brand-name {
    font-family: "Alegreya", serif; font-weight: 700; color: var(--white);
    font-size: 27px; line-height: 1.05;
  }
  .organic-seal {
    position: absolute; right: 26px; top: 34px; width: 88px; height: 88px;
    border: 2px solid var(--white); border-radius: 50%;
    display: flex; align-items: center; justify-content: center; text-align: center;
    font-family: "Merriweather Sans", sans-serif; font-style: italic; font-size: 17px; line-height: 1.15;
    transform: rotate(-14deg);
  }

  /* Front */
  .product-title {
    position: absolute; top: 163px; left: 0; right: 0; text-align: center;
    font-family: "Signika", sans-serif; font-weight: 600; color: var(--fuchsia);
    font-size: 40px; line-height: 1.08; letter-spacing: 0.5px; text-transform: uppercase;
  }
  .product-tagline {
    position: absolute; top: 256px; left: 0; right: 0; text-align: center;
    font-family: "Merriweather Sans", sans-serif; font-style: italic; font-size: 23px; letter-spacing: 0.5px;
  }
  .front-art { position: absolute; left: 0; top: 0; width: 465px; height: 728px; }
  .serving-count {
    position: absolute; left: 28px; bottom: 28px; color: var(--matte-black);
    font-family: "Signika", sans-serif; text-align: center; line-height: 0.95;
  }
  .serving-count small { display: block; font-size: 13px; letter-spacing: 1px; font-weight: 500; }
  .serving-count strong { display: block; font-size: 38px; font-weight: 600; }
  .net-weight {
    position: absolute; right: 30px; bottom: 38px; text-align: center;
    font-family: "Signika", sans-serif; line-height: 1.05;
  }
  .net-weight small { display: block; font-size: 11px; letter-spacing: 0.5px; }
  .net-weight strong { display: block; font-size: 19px; font-weight: 600; }
  .loose-leaf {
    position: absolute; left: 232px; bottom: 48px; transform: rotate(-33deg);
    font-family: "Signika", sans-serif; font-weight: 600; color: var(--white);
    font-size: 17px; letter-spacing: 2px;
  }

  /* Back */
  .back-header { position: relative; height: 150px; }
  .back-brand {
    position: absolute; left: 0; right: 0; top: 30px; text-align: center;
    font-family: "Alegreya", serif; font-weight: 700; font-size: 31px; line-height: 1.05;
  }
  .back-body { padding: 0 40px; text-align: center; }
  .section-heading {
    font-family: "Merriweather Sans", sans-serif; font-style: italic; font-weight: 600; font-size: 16px; line-height: 1.35;
  }
  .ingredients { font-size: 11.5px; color: var(--grey-text); margin-top: 8px; line-height: 1.3; }
  .steeping { display: flex; justify-content: center; gap: 40px; margin-top: 22px; }
  .steep-step { width: 80px; font-size: 9.5px; color: var(--grey-text); line-height: 1.2; }
  .steep-step svg { display: block; margin: 0 auto 8px; height: 34px; }
  .divider { height: 2px; background: linear-gradient(90deg, transparent, var(--fuchsia) 15%, var(--fuchsia) 85%, transparent); margin: 22px 20px 8px; }
  .best-sellers { display: flex; justify-content: center; gap: 14px; margin-top: 12px; }
  .seller { width: 92px; font-size: 12px; }
  .seller-thumb { width: 92px; height: 92px; background: var(--white); padding: 6px; margin-bottom: 10px; }
  .seller-thumb div { width: 100%; height: 100%; background: linear-gradient(160deg, var(--matte-black) 0 35%, var(--fuchsia) 35% 48%, #d8b650 48%, #b44a5d 100%); }
  .story { margin-top: 30px; }
  .story p { font-size: 13px; line-height: 1.2; margin-top: 10px; color: var(--white); text-align: justify; text-align-last: center; }
  .back-footer {
    position: absolute; left: 42px; right: 28px; bottom: 22px;
    display: flex; align-items: flex-end; justify-content: space-between;
  }
  .caffeine-free {
    width: 68px; height: 68px; border-radius: 50%; background: var(--white); color: var(--matte-black);
    display: flex; align-items: center; justify-content: center; text-align: center;
    font-family: "Merriweather Sans", sans-serif; font-style: italic; font-weight: 600; font-size: 13px; line-height: 1.05;
  }
  .company-info { text-align: center; font-size: 8.5px; line-height: 1.15; margin-bottom: 2px; }
  .best-by {
    display: inline-block; margin-top: 5px; background: var(--white); color: var(--matte-black);
    font-family: "Signika", sans-serif; padding: 3px 6px 2px; line-height: 1.1;
  }
  .best-by strong { display: block; font-size: 13px; font-weight: 600; }
  .best-by small { display: block; font-size: 7px; }
  .upc-space {
    width: 92px; height: 62px; background: var(--white); color: var(--matte-black);
    display: flex; align-items: center; justify-content: center;
    font-family: "Signika", sans-serif; font-weight: 600; font-size: 27px;
  }
</style>
</head>
<body>

<section class="panel panel--front" aria-label="Pouch front">
  <svg class="front-art" viewBox="0 0 465 728" aria-hidden="false">
    <defs>
      <linearGradient id="blend" x1="0" y1="0" x2="1" y2="1">
        <stop offset="0" stop-color="#d9b84e"/>
        <stop offset="0.45" stop-color="#c9a140"/>
        <stop offset="0.75" stop-color="#b5485c"/>
        <stop offset="1" stop-color="#d39a4a"/>
      </linearGradient>
    </defs>
    <path d="M0,560 C40,420 160,330 440,286 C432,470 360,640 230,728 L0,728 Z" fill="var(--fuchsia)"/>
    <path d="M0,410 C120,340 260,300 440,286 L465,286 L465,300 C300,320 120,380 0,470 Z" fill="var(--fuchsia)"/>
    <path d="M418,302 C300,318 130,370 60,470 C15,540 15,650 55,728 L190,728 C330,630 405,480 418,302 Z" fill="var(--white)"/>
    <path d="M402,318 C290,335 140,385 78,478 C38,545 36,640 70,712 L180,712 C318,620 390,480 402,318 Z" fill="url(#blend)" role="img" aria-label="Photo of the loose leaf tea blend: dried marigold flowers, quince pieces and verbena leaves"/>
    <path d="M190,728 C330,630 405,480 418,302 L440,292 C432,470 370,640 250,728 Z" fill="var(--fuchsia)"/>
  </svg>

  <div class="brand-tab"><span class="brand-name">The Brew<br>Works</span></div>
  <div class="organic-seal">100%<br>Organic</div>

  <h1 class="product-title">Quince Marigold<br>Verbena Tea</h1>
  <p class="product-tagline">Calming &amp; Soothing</p>

  <div class="serving-count"><small>MAKES</small><strong>60</strong><small>CUPS</small></div>
  <div class="loose-leaf">LOOSE LEAF</div>
  <div class="net-weight"><small>NET WT</small><strong>4 <small style="display:inline;font-size:12px">OZ.</small></strong><strong>113 <small style="display:inline;font-size:12px">G</small></strong></div>
</section>

<section class="panel panel--back" aria-label="Pouch back">
  <header class="back-header">
    <div class="back-brand">The Brew<br>Works</div>
    <div class="organic-seal">100%<br>Organic</div>
  </header>

  <div class="back-body">
    <h2 class="section-heading">Calming Loose Leaf Herbal Tea<br>Made With Superior Quality Ingredients</h2>
    <p class="ingredients">Organic marigold flowers, organic quince pieces, organic verbena leaves, organic lemon peel, organic rosehips</p>

    <div class="steeping">
      <div class="steep-step">
        <svg viewBox="0 0 34 34"><circle cx="17" cy="17" r="12" fill="none" stroke="#fff" stroke-width="2"/><path d="M17 10v7l5 3" fill="none" stroke="#fff" stroke-width="2"/></svg>
        Steeping Time<br>5-7 Mins
      </div>
      <div class="steep-step">
        <svg viewBox="0 0 20 40"><path d="M7 4a3 3 0 0 1 6 0v22a6 6 0 1 1-6 0z" fill="none" stroke="#fff" stroke-width="2"/><circle cx="10" cy="31" r="3" fill="#fff"/><path d="M10 14v15" stroke="#fff" stroke-width="2"/></svg>
        Temperature<br>206° F / 95° C
      </div>
      <div class="steep-step">
        <svg viewBox="0 0 20 40"><ellipse cx="10" cy="9" rx="5" ry="7" fill="none" stroke="#fff" stroke-width="2"/><path d="M10 16v20" stroke="#fff" stroke-width="2.5"/></svg>
        Qty per Cup<br>1-2 Heaping tsp
      </div>
    </div>

    <div class="divider"></div>
    <h2 class="section-heading">Try Our Other Best Sellers</h2>
    <div class="best-sellers">
      <div class="seller"><div class="seller-thumb"><div role="img" aria-label="Milk Oolong Tea pouch"></div></div>Milk Oolong Tea</div>
      <div class="seller"><div class="seller-thumb"><div role="img" aria-label="Rooibos Tea pouch"></div></div>Rooibos Tea</div>
      <div class="seller"><div class="seller-thumb"><div role="img" aria-label="Peppermint Tea pouch"></div></div>Peppermint Tea</div>
    </div>

    <div class="story">
      <h2 class="section-heading">Our Story... A Tradition Of Excellence</h2>
      <p>Lorem ipsum dolor sit amet, consectetuer adipiscing elit, sed diam nonummy nibh euismod tincidunt ut laoreet dolore magna aliquam erat volutpat. Ut wisi enim ad minim veniam, quis nostrud exerci tation ullamcorper suscipit lobortis nisl ut aliquip</p>
    </div>
  </div>

  <footer class="back-footer">
    <div class="caffeine-free">Caffeine<br>Free</div>
    <div class="company-info">
      The Brew Works LLC<br>418 Fernhill Rd #310<br>Dover, DE, USA 19904
      <div class="best-by"><strong>BEST BY DEC 31 2025</strong><small>LOT# BWQMV204615</small><small>STORE IN A PLACE AS COOL AS YOU</small></div>
    </div>
    <div class="upc-space">UPC</div>
  </footer>
</section>

</body>
</html>
```